Brochure Projecct

I need a brochure created for my company, which will be sent to customers via email in PDF format. I have uploaded the company logo with this project, which I want incorporated in the design.

Designers should view the company website at www.brightcounselhub.com. I want the brochure to compliment the website (i.e., very clean design). I would also like pictures added to the brochure to make the design visually stunning.

In terms of content, I need four pages in the brochure to add four separate sections of content (one section per page). The four sections of content will be as follows (1) Search Engine Optimization Benefits (2) Increased Client Retention (3) Showcase Your Law Firm (4) Maximize Your Online ROI (5) Pricing Plans. I will give the content to the winning designer to add to the project. Each individual content section will have four subsection titles after which content of approximately 100 to 200 words will appear.

Designers can decide if other pages should be added to the brochure (i.e., a "cover page" that would have little content, but be visually appealing like the cover of a book - - - a "back page" that may just have the logo, contact information, etc).

My company address and email address should be prominently featured through every page (address: 7315 West Maple Ridge Avenue, Suite 1400, Scottsdale, Arizona 85377; email: sales@brightcounselhub.com).

Industry/Entity Type

It Company

Requirements
Must have
• Clean look but visually stunning incorporating the design of the website at brightcounselhub.com as well as the logo. Also, room for content as set forth in the description of this project.

```html
<!DOCTYPE html>
<html lang="en">
<head>
<meta charset="utf-8">
<title>Showcase Your Law Firm – Bright Counsel Hub</title>
<link rel="stylesheet" href="https://fonts.googleapis.com/css2?family=Open+Sans:wght@300;400;700&display=swap">
<style>
  :root {
    --canvas-bg: #5a5a5a;
    --page-bg: #ffffff;
    --accent-red: #d42030;
    --ink: #1c1c1c;
    --panel-top: #9a9a9c;
    --panel-bottom: #626265;
    --panel-text: #ffffff;
    --footer-blue: #3069a3;
    --footer-text: #c4d6ea;
    --photo-light: #eef1f4;
    --photo-mid: #8fb3d6;
    --photo-dark: #1d1f24;
  }
  * { margin: 0; padding: 0; box-sizing: border-box; }
  html, body {
    width: 1200px;
    height: 639px;
    overflow: hidden;
    background: var(--canvas-bg);
    font-family: "Open Sans", Arial, sans-serif;
  }
  .brochure-page {
    position: absolute;
    left: 50px;
    top: 46px;
    width: 1100px;
    height: 546px;
    background: var(--page-bg);
  }
  .hero {
    position: absolute;
    left: 0;
    top: 0;
    width: 882px;
    height: 482px;
    overflow: hidden;
  }
  .hero-photo {
    position: absolute;
    inset: 0;
    background:
      radial-gradient(ellipse 210px 250px at 48% 56%, var(--photo-light) 0%, var(--photo-light) 55%, rgba(238,241,244,0) 100%),
      radial-gradient(ellipse 360px 380px at 48% 55%, var(--photo-mid) 0%, rgba(143,179,214,0.6) 55%, rgba(143,179,214,0) 100%),
      linear-gradient(90deg, #121316 0%, #2c2e33 30%, #2c2e33 70%, #121316 100%);
  }
  .hero-copy {
    position: absolute;
    left: 303px;
    top: 186px;
    width: 305px;
    color: var(--ink);
  }
  .hero-title {
    font-weight: 700;
    font-size: 45px;
    line-height: 48px;
    color: var(--accent-red);
    letter-spacing: 0.5px;
  }
  .hero-subtitle {
    font-weight: 300;
    font-size: 41px;
    line-height: 48px;
    letter-spacing: -0.5px;
    white-space: nowrap;
  }
  .hero-intro {
    margin-top: 10px;
    font-size: 11px;
    line-height: 14.5px;
    width: 300px;
  }
  .about-panel {
    position: absolute;
    left: 890px;
    top: 0;
    width: 210px;
    height: 482px;
    padding: 26px 14px 0 10px;
    background: linear-gradient(180deg, var(--panel-top) 0%, var(--panel-bottom) 100%);
    color: var(--panel-text);
    font-size: 10.6px;
    line-height: 13.3px;
  }
  .about-panel p + p { margin-top: 13px; }
  .about-panel strong { font-weight: 700; text-transform: uppercase; }
  .contact-bar {
    position: absolute;
    left: 0;
    top: 487px;
    width: 1100px;
    height: 59px;
    background: var(--footer-blue);
    color: var(--footer-text);
  }
  .contact-label {
    position: absolute;
    left: 29px;
    top: 12px;
    font-size: 14px;
    line-height: 16px;
  }
  .contact-address {
    position: absolute;
    left: 29px;
    top: 30px;
    font-size: 12px;
    line-height: 16px;
  }
  .contact-email {
    position: absolute;
    left: 742px;
    top: 29px;
    font-size: 12px;
    line-height: 16px;
  }
</style>
</head>
<body>
  <main class="brochure-page">
    <section class="hero">
      <div class="hero-photo" role="img" aria-label="Photo of a businessman in a dark suit pulling open his blue shirt and tie to reveal a white T-shirt beneath"></div>
      <div class="hero-copy">
        <h1 class="hero-title">SHOWCASE</h1>
        <h2 class="hero-subtitle">YOUR LAW FIRM</h2>
        <p class="hero-intro">The Bright Counsel Hub is different from every other law firm directory website because we have already done the difficult work to differentiate between the hundreds of lawyers on the internet to locate an experienced attorney for your particular case.</p>
      </div>
    </section>

    <aside class="about-panel">
      <p><strong>Bright Counsel Hub was created by an attorney</strong> who realized he was able to guide his own friends, family, and even his own clients to the best lawyers in other practice areas. As importantly, he was also able to steer his trusted friends and family away from lawyers and law firms that were not as capable. He was provide that valuable guideance because he pratices law in same the legal community and is, therefore, knowledgeable based upon that experience as to which lawyers produce the best results for their clients.</p>
      <p><strong>Understanding everyone does not have a lawyer</strong> in the family to help them locate an attorney, he started Bright Counsel Hub to ensure everyone has access to finding the best lawyer for his or her case. Instead of scrolling through dozens and dozens of pretty websites containing all sorts of marketing messages, Bright Counsel Hub allows you to evaluate several qualified lawyers who have an established reputation of excelling in their legal practice area.<br>Tcapable advocates for their clients.</p>
    </aside>

    <footer class="contact-bar">
      <div class="contact-label">CONTACTS:</div>
      <address class="contact-address" style="font-style:normal">7315 West Maple Ridge Avenue, Suite 1400, Scottsdale, Arizona 85377</address>
      <div class="contact-email">email: sales@brightcounselhub.com</div>
    </footer>
  </main>
</body>
</html>
```